KRV Business Cards

We are a local commercial development company based in Silicon Valley and we would like a new business card. I've attached a copy of our company brochure to give a flavor of what we do, our logo, info company colors/graphics, and our current business card. We don't necessarily need a crazy makeover, but would like something that feels a little bit more "fresh" and modern (we've had the same business card design for 15+ years), but still in keeping with our overall brand -- clean, high-quality, modern but timeless. Would like to add our website to the info on the card (www.velmara.com) and would like the flexibility for some folks to have an efax number listed and some not to have that included (without it looking like there is a hole).

```html
<!DOCTYPE html>
<html lang="en">
<head>
<meta charset="utf-8">
<title>KRV Business Cards</title>
<link rel="stylesheet" href="https://fonts.googleapis.com/css2?family=Cinzel:wght@400&family=Work+Sans:wght@400;600;700&display=swap">
<style>
  :root {
    --stage: #e9eaec;
    --brand-blue: #3a5874;
    --brand-navy: #2c4a66;
    --paper: #ffffff;
    --ink-soft: #4a4f55;
    --on-blue: #ffffff;
  }
  * { box-sizing: border-box; margin: 0; padding: 0; }
  html, body {
    width: 1200px; height: 800px; overflow: hidden;
    background: var(--stage);
  }
  .canvas {
    position: relative; width: 1200px; height: 800px;
  }
  .card {
    position: absolute; top: 257px;
    width: 500px; height: 286px;
    box-shadow: 0 6px 18px rgba(0,0,0,0.18);
  }
  .card--front { left: 70px; background: var(--brand-blue); }
  .card--back  { left: 630px; background: var(--paper); }

  .company-name {
    position: absolute; left: 34px; bottom: 34px;
    font-family: "Cinzel", serif; font-weight: 400;
    color: var(--on-blue); font-size: 34px; line-height: 1.0;
    letter-spacing: 0.5px;
  }
  .company-name .suffix { font-size: 24px; }
  .front-web {
    position: absolute; right: 30px; bottom: 112px;
    font-family: "Work Sans", sans-serif; font-weight: 700;
    font-size: 13px; color: var(--on-blue);
  }

  .rule {
    position: absolute; left: 150px; right: 30px; top: 186px;
    height: 1px; background: var(--brand-navy);
  }
  .holder { position: absolute; left: 34px; top: 162px; }
  .holder-name {
    font-family: "Work Sans", sans-serif; font-weight: 700;
    font-size: 18px; letter-spacing: 1px; color: var(--brand-navy);
  }
  .holder-title {
    font-family: "Work Sans", sans-serif; font-weight: 400;
    font-size: 14px; color: var(--brand-navy); margin-top: 2px; margin-left: 4px;
  }
  .contact, .address {
    position: absolute; list-style: none;
    font-family: "Work Sans", sans-serif; font-size: 12.5px;
    color: var(--ink-soft); line-height: 1.45;
  }
  .contact { left: 38px; top: 222px; }
  .address { left: 318px; top: 168px; }
  .label { font-weight: 600; color: var(--brand-navy); }
</style>
</head>
<body>
<main class="canvas">
  <section class="card card--front" aria-label="Card front">
    <h1 class="company-name">Velmara<br>Development<br>Company, <span class="suffix">LLC</span></h1>
    <p class="front-web">www.velmara.com</p>
  </section>

  <section class="card card--back" aria-label="Card back">
    <div class="rule"></div>
    <div class="holder">
      <p class="holder-name">JANINE R.HOLLOWAY</p>
      <p class="holder-title">Partner</p>
    </div>
    <ul class="contact">
      <li><span class="label">Phone:</span> (08) 7412 5590</li>
      <li><span class="label">Email:</span> mobile@velmara.com</li>
      <li><span class="label">Web:</span> www.velmara.com</li>
    </ul>
    <ul class="address">
      <li><span class="label">Address:</span></li>
      <li>288 Linden Street</li>
      <li>Mountain View, California 94041</li>
    </ul>
  </section>
</main>
</body>
</html>
```